College presentation for a startup bootcamp - how to talk to customers

I need a simple design for a college PowerPoint/ google slide presentation for students that are going through a Startup BootCamp. No flashy colors
- Accessible font - or provide the font - I like the vorel's website font or normal text font
- use a neutral colors schemes of grays - with 1-2 highlight colors
- You can use the photos in the presentation or others
- Urgent the presentation is on Thursday - I will award the winner on Wednesday.
- It's 23 slides long.

Target Market(s)

College students interested in startups

Industry/Entity Type

College

Font styles to use
Serif
Sans Serif
Other font styles liked:
• helvetica

Colors

Designer to choose only greyscale colors for use in the design.

Requirements
Must have
• clean , simple design neural colors like greyscale with 1-3 pop colors
Should not have
• no flashy colors, or hard to read text

```html
<!DOCTYPE html>
<html lang="en">
<head>
<meta charset="utf-8">
<title>Customer Development – Mom's test</title>
<link rel="stylesheet" href="https://fonts.googleapis.com/css2?family=Roboto:ital,wght@0,300;0,400;0,500;0,700;1,400&display=swap">
<style>
:root{
  --page:#dfe2e0;
  --white:#ffffff;
  --tan:#b8a386;
  --tan-light:#e8ddd0;
  --gold:#a8875e;
  --brown:#6b2e1e;
  --ink:#5e5955;
  --ink-soft:#8a847e;
  --clay:#b98c6c;
  --line:#c9b79f;
}
*{box-sizing:border-box;margin:0;padding:0}
html,body{width:668px;height:1200px;overflow:hidden}
body{background:var(--page);font-family:"Roboto",Helvetica,Arial,sans-serif;color:var(--ink)}
.deck{position:absolute;left:35px;top:252px;width:598px;display:grid;grid-template-columns:290px 290px;column-gap:18px;row-gap:15px}
.slide{position:relative;width:290px;height:163px;background:var(--white);overflow:hidden;box-shadow:0 4px 8px rgba(0,0,0,.18)}
.footer-rule{position:absolute;left:0;right:0;top:156px;height:1px;background:var(--line)}
.page-no{position:absolute;right:4px;top:152px;width:7px;height:7px;background:var(--tan);color:#fff;font-size:3.5px;text-align:center;line-height:7px}
.header-band{position:absolute;left:0;top:8px;width:175px;height:18px;background:linear-gradient(90deg,var(--tan) 62%,rgba(184,163,134,0));color:#fff;font-size:9.5px;font-weight:300;line-height:18px;padding-left:13px;white-space:nowrap}
.header-band b{font-weight:700}
.header-band .accent{color:var(--brown);font-weight:400}

/* cover */
.cover{background:var(--tan-light)}
.cover-photo{position:absolute;inset:0;background:linear-gradient(100deg,#e9e0d6 0%,#e6dbcf 45%,#d9c8b8 70%,#e3d8cc 100%)}
.cover-rule{position:absolute;left:9px;top:15px;width:1px;height:135px;background:var(--gold)}
.cover-title{position:absolute;left:23px;top:70px;font-size:18px;font-weight:700;line-height:22px;color:#7a716a;letter-spacing:.2px}
.cover-sub{position:absolute;left:23px;top:117px;font-size:10.5px;font-weight:400;color:#7a716a}

/* agenda */
.agenda-tag{position:absolute;left:0;top:45px;width:60px;height:18px;background:var(--tan);color:#fff;font-size:9.5px;font-weight:300;line-height:18px;padding-left:10px}
.agenda-head{position:absolute;left:67px;top:49px;font-size:7.5px;font-weight:700;color:var(--ink)}
.agenda-list{position:absolute;left:67px;top:66px;width:130px;list-style:none;border-top:1px solid var(--line)}
.agenda-list li{height:17.5px;border-bottom:1px solid var(--line);font-size:7px;line-height:17px;padding-left:6px}
.agenda-list li::before{content:"•";margin-right:8px}

/* framework diagram */
.stage{position:absolute;top:37px;height:92px;border:1px solid var(--line);border-radius:4px}
.stage-name{font-size:4.6px;font-weight:700;text-align:center;line-height:5.5px;padding:3px 2px;border-bottom:1px solid var(--line);color:var(--ink)}
.step{margin:4px auto 0;width:38px;border:1px solid var(--line);border-radius:3px;font-size:4px;text-align:center;line-height:4.8px;padding:3px 1px;color:var(--ink-soft)}
.step.tall{height:64px;padding-top:26px}
.step.half{height:30px;padding-top:9px}
.pivot{position:absolute;left:52px;top:128px}
.credit{position:absolute;right:18px;top:148px;font-size:2.6px;font-weight:700;color:var(--ink)}

/* quote slide */
.quote-panel{position:absolute;left:5px;top:9px;width:280px;height:138px;background:linear-gradient(90deg,#fff 10%,#efe7dd 50%,var(--tan) 100%)}
.quote-text{position:absolute;left:30px;top:40px;width:110px;text-align:center;font-size:6px;line-height:12.3px;color:var(--ink)}
.quote-text .gold{color:var(--gold);font-weight:500}
.quote-text .lie{color:var(--brown);font-weight:700}
.quote-text .dark{color:var(--brown)}
.quote-text .problem{color:var(--gold);font-weight:700;font-size:7px}
.quote-photo{position:absolute;left:145px;top:38px;width:125px;height:83px;background:linear-gradient(120deg,#f3ebe2,#e6d4c2 55%,#efe1d3)}

/* dialogue slides */
.dialogue{position:absolute;left:16px;top:41px;width:260px;list-style:none;font-size:6.2px;line-height:7.8px;color:var(--ink)}
.dialogue li{padding-left:5px;text-indent:-5px}
.dialogue li::before{content:"• "}
.dialogue b{color:var(--brown);font-weight:700}
.dialogue b.mom{color:var(--ink-soft)}
.dialogue .thought{padding-left:20px;text-indent:-5px;color:var(--gold);font-size:5.2px;line-height:6.4px;margin:1px 0 2px}
.dialogue .thought::before{content:"• ";color:var(--ink)}
.dialogue .blank{padding-left:20px;color:var(--gold);font-size:5px;margin:1px 0 2px}

.ask-label{position:absolute;left:15px;top:42px;font-size:6.8px;font-weight:700;color:var(--brown)}
.ask-list{position:absolute;left:22px;top:57px;list-style:none;font-size:6.5px;line-height:12.2px;color:var(--ink)}
.ask-list li::before{content:"•";margin-right:6px}

/* closing */
.closing{background:var(--clay)}
.closing-photo{position:absolute;left:130px;top:0;width:160px;height:163px;background:linear-gradient(110deg,var(--clay) 0%,#c7a687 40%,#b79a78 100%)}
.closing-title{position:absolute;left:15px;top:15px;font-size:26px;line-height:29px;color:#fff;font-weight:300}
.closing-title b{font-weight:700}
.closing-rule{position:absolute;left:8px;width:114px;height:1px;background:rgba(255,255,255,.8)}
.closing-name{position:absolute;left:15px;top:110px;font-size:10px;font-weight:700;color:#fff}
.closing-info{position:absolute;left:15px;top:135px;font-size:7.2px;line-height:9px;color:#fff}
.closing-info u{text-decoration:underline}
</style>
</head>
<body>
<main class="deck">

  <section class="slide cover">
    <div class="cover-photo" role="img" aria-label="Soft beige photo of a smiling café owner behind a counter"></div>
    <div class="cover-rule"></div>
    <h1 class="cover-title">CUSTOMER<br>DEVELOPMENT</h1>
    <p class="cover-sub">Mom’s test - how to talk to customers</p>
  </section>

  <section class="slide agenda">
    <div class="agenda-tag">AGENDA</div>
    <p class="agenda-head">Mom’s test:</p>
    <ul class="agenda-list">
      <li>What is the problem?</li>
      <li>How to talk to customers ?</li>
      <li>How to ask questions?</li>
      <li>Who to talk to?</li>
    </ul>
    <div class="footer-rule"></div><div class="page-no">2</div>
  </section>

  <section class="slide framework">
    <div class="header-band">Customer Development</div>
    <div class="stage" style="left:37px;width:50px">
      <div class="stage-name">Customer<br>Discovery</div>
      <div class="step">Problem-<br>Solution Fit</div>
      <div class="step">Proposed<br>MVP</div>
      <div class="step">Proposed<br>Funnel(s)</div>
    </div>
    <div class="stage" style="left:91px;width:53px">
      <div class="stage-name">Customer<br>Validation</div>
      <div class="step">Product-<br>Market Fit</div>
      <div class="step">Business<br>Model</div>
      <div class="step">Sales &amp; Marketing<br>Roadmap</div>
    </div>
    <div class="stage" style="left:153px;width:50px">
      <div class="stage-name">Customer<br>Creation</div>
      <div class="step tall">Scale<br>Execution</div>
    </div>
    <div class="stage" style="left:207px;width:50px">
      <div class="stage-name">Company<br>Building</div>
      <div class="step half">Scale<br>Organization</div>
      <div class="step half">Scale<br>Operations</div>
    </div>
    <svg class="pivot" width="30" height="16" viewBox="0 0 30 16" aria-hidden="true">
      <path d="M24 2 C22 9 10 9 7 4" fill="none" stroke="#5e5955" stroke-width="1.4"/>
      <path d="M4 3 L8 2 L7 6 Z" fill="#5e5955"/>
      <text x="10" y="15" font-size="4.5" font-weight="700" fill="#6b2e1e" font-family="Roboto,sans-serif">pivot</text>
    </svg>
    <p class="credit">Lena Ortiz's Customer Development by Theo Marsh, devpath.org</p>
    <div class="footer-rule"></div><div class="page-no">3</div>
  </section>

  <section class="slide quote">
    <div class="quote-panel"></div>
    <p class="quote-text">
      People try to be <span class="gold">nice</span><br>
      Therefore they <span class="lie">lie</span> in your face<br>
      <span class="gold">without realizing</span> it<br><br>
      <span class="dark">Bad data it worse than no data</span><br>
      E.g. <i>“I’ll definitely buy that”</i><br>
      <span class="problem">THE PROBLEM</span>
    </p>
    <div class="quote-photo" role="img" aria-label="Photo of a smiling woman holding a smiley-face balloon"></div>
    <div class="footer-rule"></div><div class="page-no">4</div>
  </section>

  <section class="slide">
    <div class="header-band"><b>Mom’s test</b> &nbsp;- What people <span class="accent">say</span></div>
    <ul class="dialogue">
      <li><b>You:</b> Mom, I have a business idea. Do you have 5 mins?</li>
      <li><b class="mom">Mom:</b> Of course, dear</li>
      <li class="blank">……………………</li>
      <li><b>You:</b> You life your Lumo tablet and use it a lot?</li>
      <li><b class="mom">Mom:</b> Sure it’s great.</li>
      <li class="blank">……………………</li>
      <li><b>You:</b> Would you buy a cookbook app?</li>
      <li><b class="mom">Mom:</b> I love cookbooks, sounds nice. Does it come with vegan recipes? Or something special for Xmas?</li>
      <li class="blank">……………………</li>
    </ul>
    <div class="footer-rule"></div><div class="page-no">5</div>
  </section>

  <section class="slide">
    <div class="header-band"><b>Mom’s test</b> &nbsp;- What people <span class="accent">think</span></div>
    <ul class="dialogue">
      <li><b>You:</b> Mom, I have a business idea. Do you have 5 mins?</li>
      <li><b class="mom">Mom:</b> Of course, dear</li>
      <li class="thought">I’m proud of you and I don’t want to hurt your feelings</li>
      <li><b>You:</b> You life your Lumo tablet and use it a lot?</li>
      <li><b class="mom">Mom:</b> Sure it’s great.</li>
      <li class="thought">I use it to check email on the sofa</li>
      <li><b>You:</b> Would you buy a cookbook app?</li>
      <li><b class="mom">Mom:</b> I love cookbooks, sounds nice. Does it come with vegan recipes? Or something special for Xmas?</li>
      <li class="thought">Well, I have plenty of cookbooks. I don’t need a computer in my kitchen - It might get dirty! But hey, if my kid made it, I’ll try it. App? I never bought an app. Don’t you need to enter your credit card for that? Let me try to change the subject.</li>
    </ul>
    <div class="footer-rule"></div><div class="page-no">6</div>
  </section>

  <section class="slide">
    <div class="header-band"><b>Mom’s test</b> &nbsp;- <span class="accent">How to do it right</span></div>
    <p class="ask-label">You:</p>
    <ul class="ask-list">
      <li>Mom, when have you last time used the Lumo tablet?</li>
      <li>For what?</li>
      <li>Have you ever used it in the kitchen?</li>
      <li>Have you ever bought an app? Which? Why? For how much?</li>
      <li>Do you use your cookbooks</li>
      <li>Is there anything you dislike about them?</li>
      <li>What was the last cookbook you bought? When? Why?</li>
    </ul>
    <div class="footer-rule"></div><div class="page-no">7</div>
  </section>

  <section class="slide closing">
    <div class="closing-photo" role="img" aria-label="Paper cut-out speech bubbles with question marks"></div>
    <h2 class="closing-title">THANK<br><b>YOU!</b></h2>
    <div class="closing-rule" style="top:107px"></div>
    <p class="closing-name">Mara Lentz</p>
    <div class="closing-rule" style="top:128px"></div>
    <p class="closing-info">Co-Founder Northway Learning<br><u>maralentz</u>@postbox.io</p>
  </section>

</main>
</body>
</html>
```